7 D Thinking

Re: Personal development plan based on reflection & introspection

To do

• One pager as shown in the uploaded files ( the blue version )
• Small Power Point with 7 or 8 slides

Title :

Disruptive people have 7 D Thinking Mindsets

1) Dissatisfied
----------------
2) Dream
3) Desire
4) Determination
5) Discipline
6) Drive
----------------
7) Disrupt

To be used for
• For a One on one discussion
• A personal Digital Intake call via my website
• Power Point presentation 7or 8 slides

Basis for the one pager and PPT

 
Please find herewith 2 documents related to 5-Dimensional Thinking
 
I use this canvas to question myself or help friends.
 
Getting older and wiser I added a 6th and 7th dimension: Dissatisfaction & Disruption.

Sources about me
https://www.maxorlanfield.lu/
https://www.maxorlanfield.lu/who-i-am-2/
http://pooledideasforum.com/about/
https://www.profilenet.com/in/morlanfield/?ppe=1

Topics to bring on the one pager & PPT

 
1. Dissatisfied 

2. Dream
3.  Desire
4. Determination
5. Discipline
6.  Drive

7. Disrupted

Style & Colors

• My favorite color is Blue
• My disruptive color is RED

Disruption :meaning
specialized business to change the traditional way that an industry operates, especially in a new and effective way:
Korvane Inc. disrupted the traditional way of selling computers by switching to the internet.
Examples from the crowdsourced world Zivo, Nestora etc..

 
How do you start your introspection?
 
A  Write down on a paper how Dissatisfied you are with your actual situation.
 
B  Go to the loop and start with defining your Dream and follow the method.
 
C  Find out how you can be a Disruptor for yourself or others
Updates

Reason: Ok,it is the first time I use SketchHive. I did set up a poll Did not receive meaningfull feed back so far I will decide in 5 days so please extend Maxime

Target Market(s)

People who are dissatisfied with their life either from PRIVATE either from PROFESSIONAL point of view
High level educated people, business related , being able to make up their -personal change plan.

Industry/Entity Type

Business Consultant

Font styles to use
Other font styles liked:
• Helvetica, Arial

Colors
ec1f27
0355a3
ffffff

Requirements
Must have
• 2 circles / loops
• A loop starting with
• 1 -Dissatisfied ( I am not happy with my life personal /business- I want change )
• ending with
• 7 Disrupt
• All words by topic (1 to 7 ) you find on the uploaded files
• A inner loop with the 5 initial D,s
Nice to have
• a movement , 2 cirlces
• business style
• I am a consultant
• Wanting to help people creating a better world by giving them a tool for reflection to re-invent themselves
Should not have
• gender related words

```html
<!DOCTYPE html>
<html lang="en">
<head>
<meta charset="utf-8">
<title>Disruptive people have 7 D Thinking mindsets</title>
<link href="https://fonts.googleapis.com/css2?family=Lato:wght@400;700;900&display=swap" rel="stylesheet">
<style>
  :root {
    --brand-blue: #0355a3;
    --disrupt-red: #ec1f27;
    --white: #ffffff;
    --mind-yellow: #ffff00;
    --label-blue: #2f5f8f;
    --footer-blue: #2e5b8a;
    --sky-top: #1a68c4;
    --sky-mid: #5d9bd8;
    --sky-low: #b7d3ec;
    --field: #c9b27a;
    --mind-dark: #1e3f6e;
    --mind-light: #4477b3;
  }
  * { margin: 0; padding: 0; box-sizing: border-box; }
  html, body { width: 1200px; height: 675px; overflow: hidden; background: var(--white); }
  body { font-family: "Lato", Arial, Helvetica, sans-serif; }

  .poster { position: relative; width: 1200px; height: 675px; overflow: hidden; }

  .landscape {
    position: absolute; inset: 0 0 50px 0;
    background: linear-gradient(180deg, var(--sky-top) 0%, var(--sky-mid) 45%, var(--sky-low) 84%, var(--field) 93%, #8a9a55 100%);
  }

  .headline {
    position: absolute; top: 22px; left: 0; width: 100%;
    text-align: center; color: var(--white);
    font-weight: 700; font-size: 38px; letter-spacing: 0.2px;
  }
  .headline .highlight { color: var(--mind-yellow); font-size: 44px; }

  .mind-area {
    position: absolute; left: 452px; top: 185px; width: 308px; height: 327px;
    border-radius: 46% 46% 42% 42% / 38% 38% 56% 56%;
    background: radial-gradient(ellipse at 50% 45%, var(--mind-light) 0%, var(--mind-dark) 100%);
    opacity: 0.9;
  }

  .loops { position: absolute; inset: 0; }

  .mind-words {
    position: absolute; left: 446px; top: 226px; width: 300px;
    text-align: center; color: var(--mind-yellow);
    font-weight: 700; font-size: 32px; line-height: 48px;
    list-style: none;
  }

  .loop-label {
    position: absolute; top: 318px;
    font-weight: 900; font-size: 31px; letter-spacing: 0.3px;
    text-shadow: -1.5px -1.5px 0 var(--white), 1.5px -1.5px 0 var(--white),
                 -1.5px 1.5px 0 var(--white), 1.5px 1.5px 0 var(--white);
  }
  .loop-label--start { left: 165px; color: var(--label-blue); }
  .loop-label--end { left: 847px; color: var(--disrupt-red); }

  .contact-bar {
    position: absolute; left: 0; bottom: 0; width: 100%; height: 50px;
    background: var(--footer-blue);
    color: var(--white); font-size: 16px; font-weight: 700;
  }
  .contact-item { position: absolute; top: 0; height: 50px; display: flex; align-items: center; gap: 10px; }
  .contact-item svg { width: 30px; height: 30px; flex: none; }
  .contact-item--phone { left: 40px; }
  .contact-item--mail { left: 255px; }
  .contact-item--place { left: 522px; }
  .contact-item--social { left: 958px; }
</style>
</head>
<body>
<main class="poster">
  <div class="landscape" role="img" aria-label="Photo of a clear blue sky over flat farmland with a row of wind turbines"></div>

  <h1 class="headline">Disruptive people have <span class="highlight">7 D Thinking</span> mindsets</h1>

  <div class="mind-area" role="img" aria-label="Illustration of a human brain in dark blue tones"></div>

  <svg class="loops" width="1200" height="675" viewBox="0 0 1200 675" aria-hidden="true">
    <ellipse cx="475" cy="344" rx="325" ry="234" fill="none" stroke="var(--disrupt-red)" stroke-width="3.5"/>
    <ellipse cx="716" cy="344" rx="326" ry="234" fill="none" stroke="var(--disrupt-red)" stroke-width="3.5"/>
  </svg>

  <ol class="mind-words">
    <li>Dream</li>
    <li>Desire</li>
    <li>Determination</li>
    <li>Discipline</li>
    <li>Drive</li>
  </ol>

  <div class="loop-label loop-label--start">DISSATISFIED</div>
  <div class="loop-label loop-label--end">DISRUPT</div>

  <footer class="contact-bar">
    <div class="contact-item contact-item--phone">
      <svg viewBox="0 0 30 30" aria-hidden="true">
        <circle cx="15" cy="15" r="14" fill="var(--white)"/>
        <path d="M10.5 8 L13 8 L14 12 L12.5 13.3 C13.3 15.2 14.8 16.7 16.7 17.5 L18 16 L22 17 L22 19.5 C22 20.6 21 21.5 19.8 21.3 C14 20.5 9.5 16 8.7 10.2 C8.5 9 9.4 8 10.5 8 Z" fill="var(--footer-blue)"/>
      </svg>
      <span>00 352 621 555 014</span>
    </div>
    <div class="contact-item contact-item--mail">
      <svg viewBox="0 0 30 30" aria-hidden="true">
        <circle cx="15" cy="15" r="14" fill="var(--white)"/>
        <rect x="8" y="10" width="14" height="10" rx="1" fill="var(--footer-blue)"/>
        <path d="M8.5 10.5 L15 15.5 L21.5 10.5" fill="none" stroke="var(--white)" stroke-width="1.4"/>
      </svg>
      <span>maxime@maxorlanfield.lu</span>
    </div>
    <div class="contact-item contact-item--place">
      <svg viewBox="0 0 30 30" aria-hidden="true">
        <circle cx="15" cy="15" r="14" fill="var(--white)"/>
        <path d="M15 7 C11.7 7 9.5 9.4 9.5 12.3 C9.5 16 15 23 15 23 C15 23 20.5 16 20.5 12.3 C20.5 9.4 18.3 7 15 7 Z" fill="var(--footer-blue)"/>
        <circle cx="15" cy="12.4" r="2.2" fill="var(--white)"/>
      </svg>
      <span>Rue des Tilleuls 12, Belvaux 4410, Luxembourg</span>
    </div>
    <div class="contact-item contact-item--social">
      <svg viewBox="0 0 30 30" aria-hidden="true">
        <circle cx="15" cy="15" r="14" fill="var(--white)"/>
        <path d="M8 9.5 H22 V18.5 H14 L10.5 21.5 V18.5 H8 Z" fill="var(--footer-blue)"/>
      </svg>
      <span>@OrlanfieldMaxime</span>
    </div>
  </footer>
</main>
</body>
</html>
```